Verpackungsdesign für Zigarre
Zielgruppe
KALUN isteine Unternehmung im Baunebenbereich welche sich auf Kabelschächte und Schachtabdeckungen aus Chromstahl spezialisiert hat. Unsere Kunden sind Ingenieure, Planer, Netzbetreiber aus Telecom, Verkehr, Elektro und Industrie. Absatzpartner/Mittler sind auch grössere Bauunternehmungen. Die Ansprechpartner sind meist männlich zwischen 40 und 60 Jahre alt. Wir möchten unseren ausgewählten Kunden neben einer guten Flasche Rum welche wir schon separat gelabelt haben auch eine eigene Zigarre als Geschenk überreichen, da der Inhaber mit manchen Kunden die Leidenschaft Zigarren und Rum teilt. Dazu haben wir vorab1000 Zigarren in der Dominikanischen Republik nach den eigenen Vorgaben herstellen lassen welche, wir jetzt noch mit Banderole ausstatten möchten. Wir suchen ein schönes Design der Banderole (Bauchbinde) und auch eine kreative Verpackung für Gebinde von mehreren Zigarren (z.B. ein Einmachglas mit Etikette anstatt der Holzkistchen welche leider immer nach Gebrauch weggeschmissen werden)
Aufgabenstellung
Die Marke KALUN muss auf der Banderole als Sponsor (oder Überreicher) vermittelt werden. Für die Zigarre selbst haben wir den Namen vonerika ausgewählt. Da dies die erste eigene Zigarre wird soll der Beinamen Edition Eins verwendet werden. Evt. kann auch mit 2 Bauchbinden gearbeitet werden (KALUN und von erika und Edition Typ Eins separat... oder so...Wir benötigen ein Design und Format welches auch kurzfristig recht preisgünstig produziert werden kann. Erwartet wird ein Vorschlag bei welchem die Produktionsmöglichkeit abgeklärt wird (1000 - 5000 Stk. als Erstserie inkl. Druckofferte) Vielleicht bringt auch jemand einen ganz neuen kreativen schönen Vorschlag der Beschriftung...? Wir sind nicht auf Standardpapier eingeschossen - es muss einfach schön, kostengünstig und vorallem einprägsam sein. Bei Erfolg der Aktion überlegen wir uns noch weitere Formate und Zigarren herzustellen und vielleicht auch zu verkaufen anstatt zu verschen unter dem Namen von erika. Für die Verpackung von ganzen Gebinden (10-20 Stk. / Gebinde) suchen wir noch eine kreative Lösung welche sich von den klassischen Holzkistchen unterscheidet. Wir würden uns als Zusatz wünschen, dass der Designer auch dazu Vorschläge mit Beschriftung bringt. Die Farben von KALUN sind rot, chrom und schwarz... (siehe Website www.kalun-beispiel.com) von erika stelel ich mir in Gold vor. Evt. können die Firmenfarben von KALUN untergeordnet vertreten sein um dann komplett nur noch auf den Namen von erika später ohne KALUN mit Nachfolgeprodukten aufzusetzen um diese auch zu verkaufen.

```html
<!DOCTYPE html>
<html lang="de">
<head>
<meta charset="utf-8">
<title>von erika – Banderolen Varianten 2.1 bis 2.4</title>
<link rel="stylesheet" href="https://fonts.googleapis.com/css2?family=Caveat+Brush&family=Great+Vibes&family=Montserrat:ital,wght@0,500;1,800&display=swap">
<style>
  :root {
    --page: #ffffff;
    --label: #1a1a1a;
    --cigar-light: #c9a06c;
    --cigar-mid: #b98d58;
    --cigar-dark: #9c7442;
    --parchment-light: #fbf1d6;
    --parchment-mid: #ecd3a0;
    --parchment-dark: #c99a5a;
    --gold-light: #fbe9a6;
    --gold-mid: #e9c766;
    --gold-dark: #c9a23e;
    --seal-ring: #c9a23e;
    --seal-inner: #f1d06a;
    --ink: #111111;
  }
  * { box-sizing: border-box; margin: 0; padding: 0; }
  html, body { width: 1200px; height: 377px; overflow: hidden; background: var(--page); }
  .board { position: relative; width: 1200px; height: 377px; }
  .variant { position: absolute; top: 0; width: 300px; height: 377px; }
  .variant--1 { left: 0; }
  .variant--2 { left: 300px; }
  .variant--3 { left: 601px; }
  .variant--4 { left: 901px; }

  .variant__label {
    position: absolute; left: 16px; top: 139px;
    transform: rotate(-90deg); transform-origin: left top;
    font: 500 15px/1 "Montserrat", sans-serif; letter-spacing: 0.5px;
    color: var(--label); white-space: nowrap;
  }

  .cigar {
    position: absolute; left: 101px; top: 42px; width: 100px; height: 335px;
    border-radius: 24px 24px 0 0;
    background: linear-gradient(90deg, var(--cigar-dark), var(--cigar-light) 35%, var(--cigar-mid) 70%, var(--cigar-dark));
  }

  .band-arch {
    position: absolute; left: 117px; top: 194px; width: 68px; height: 68px;
    border-radius: 50%;
    background: radial-gradient(circle at 50% 40%, var(--parchment-light), var(--parchment-mid));
  }
  .band-main {
    position: absolute; left: 21px; width: 262px; height: 61px;
    background: linear-gradient(100deg, var(--parchment-dark), var(--parchment-mid) 25%, var(--parchment-light) 60%, var(--parchment-mid));
  }
  .variant--1 .band-main, .variant--2 .band-main { top: 226px; }
  .variant--3 .band-main, .variant--4 .band-main { top: 216px; }

  .ship-art {
    position: absolute; left: 131px; top: 203px; width: 40px; height: 44px;
    border-radius: 6px; background: linear-gradient(180deg, #3a3a3a, #111);
    opacity: 0.85;
  }

  .brand-name {
    position: absolute; left: 21px; width: 262px; text-align: center;
    color: var(--ink); white-space: nowrap;
  }
  .brand-name--brush { top: 232px; font: 52px/1 "Caveat Brush", cursive; }
  .brand-name--script { top: 228px; font: 50px/1 "Great Vibes", cursive; }
  .variant--3 .brand-name--script { top: 218px; }
  .variant--4 .brand-name--script { top: 216px; font-size: 52px; }

  .band-sub {
    position: absolute; left: 21px; width: 262px;
    background: linear-gradient(90deg, var(--gold-mid), var(--gold-light) 50%, var(--gold-mid));
    color: var(--ink);
  }
  .band-sub--narrow {
    top: 290px; height: 15px; text-align: center;
    font: 500 9px/15px "Montserrat", sans-serif; letter-spacing: 0.3px;
    border-top: 1px solid var(--gold-dark); border-bottom: 1px solid var(--gold-dark);
  }
  .band-sub--wide {
    top: 281px; height: 25px;
    font: italic 800 9px/25px "Montserrat", sans-serif;
  }
  .band-sub__from { position: absolute; left: 37px; }
  .band-sub__edition { position: absolute; left: 158px; }

  .seal {
    position: absolute; left: 131px; top: 271px; width: 42px; height: 42px;
    border-radius: 50%; background: var(--seal-ring);
  }
  .seal__inner {
    position: absolute; left: 5px; top: 5px; width: 32px; height: 32px;
    border-radius: 50%; background: var(--seal-inner);
  }
  .seal__art {
    position: absolute; left: 7px; top: 6px; width: 18px; height: 20px;
    border-radius: 4px; background: #1d1d1d; opacity: 0.85;
  }
  sup { font-size: 0.6em; vertical-align: 0.5em; }
</style>
</head>
<body>
<main class="board">

  <section class="variant variant--1">
    <div class="variant__label">VERSION 2.1</div>
    <div class="cigar" role="img" aria-label="Foto einer Zigarre mit hellem Deckblatt"></div>
    <div class="band-arch" role="img" aria-label="Pergament-Landkartenmotiv"></div>
    <div class="band-main" role="img" aria-label="Pergament-Landkartenmotiv"></div>
    <div class="ship-art" role="img" aria-label="Illustration eines Segelschiffs"></div>
    <div class="brand-name brand-name--brush">von erika</div>
    <div class="band-sub band-sub--narrow">KALUN<sup>®</sup> – EDITION EINS</div>
  </section>

  <section class="variant variant--2">
    <div class="variant__label">VERSION 2.2</div>
    <div class="cigar" role="img" aria-label="Foto einer Zigarre mit hellem Deckblatt"></div>
    <div class="band-arch" role="img" aria-label="Pergament-Landkartenmotiv"></div>
    <div class="band-main" role="img" aria-label="Pergament-Landkartenmotiv"></div>
    <div class="ship-art" role="img" aria-label="Illustration eines Segelschiffs"></div>
    <div class="brand-name brand-name--script">von Erika</div>
    <div class="band-sub band-sub--narrow">KALUN<sup>®</sup> – EDITION EINS</div>
  </section>

  <section class="variant variant--3">
    <div class="variant__label">VERSION 2.3</div>
    <div class="cigar" role="img" aria-label="Foto einer Zigarre mit hellem Deckblatt"></div>
    <div class="band-main" role="img" aria-label="Pergament-Landkartenmotiv"></div>
    <div class="brand-name brand-name--script">von Erika</div>
    <div class="band-sub band-sub--wide">
      <span class="band-sub__from">FROM KALUN<sup>®</sup></span>
      <span class="band-sub__edition">EDITION EINS</span>
    </div>
    <div class="seal"><div class="seal__inner"><div class="seal__art" role="img" aria-label="Illustration eines Segelschiffs"></div></div></div>
  </section>

  <section class="variant variant--4">
    <div class="variant__label">VERSION 2.4</div>
    <div class="cigar" role="img" aria-label="Foto einer Zigarre mit hellem Deckblatt"></div>
    <div class="band-main" role="img" aria-label="Pergament-Landkartenmotiv"></div>
    <div class="brand-name brand-name--script">von Erika</div>
    <div class="band-sub band-sub--wide">
      <span class="band-sub__from">FROM KALUN<sup>®</sup></span>
      <span class="band-sub__edition">EDITION EINS</span>
    </div>
    <div class="seal"><div class="seal__inner"><div class="seal__art" role="img" aria-label="Illustration eines Segelschiffs"></div></div></div>
  </section>

</main>
</body>
</html>
```